Olive Oil bottle label front and back

We need a label designed for an olive oil bottle along with a company logo. I have attached the bottle and the exact design of the bottle.

Our company is called Verdanto Crest Imports LLC but our olive oil will be called Verdanto Crest

Front - as you are looking at the bottle the handle will be to the right

Our logo
Kalamata Protected Designation of Origin stamp - if you can not find this leave a spot for it and the factory can add it
ISO certified protected designated Origin stamp - if you can not find this leave a spot for it and the factory can add it
Look Greek, simple, elegant
Look expensive
What type of oil - extra virgin, organic.

Back

Greek flag
Nutrition facts
Bar code just leave a white space for this
Website http://verdantocrestimports.example
Factory info - Kalamata, Greece
Best by date/made on date
Leave a space for company address

This link takes you to the bottle maker http://www.morvetta-bottleworks.example/en/products/oil-vinegar/item/512-40721

Target Market(s)

We are going to be starting to sell to upscale grocery stores and specialty food stores.

Industry/Entity Type

Food Production

Requirements
Must have
• Have gold in it because of the name and logo but not shinny, old fashioned looking gold. We want more of that simple elegant looking gold.

```html
<!DOCTYPE html>
<html lang="en">
<head>
<meta charset="utf-8">
<title>Verdanto Crest Olive Oil – Front and Back Labels</title>
<link rel="stylesheet" href="https://fonts.googleapis.com/css2?family=Montserrat:wght@600;700;800&family=Playfair+Display:wght@700;900&family=Roboto+Condensed:wght@400&family=Archivo:wght@400;800;900&display=swap">
<style>
  :root {
    --page: #ffffff;
    --label-green: #10290c;
    --label-green-deep: #0b1d08;
    --key-green: #1d4413;
    --gold: #d6a92e;
    --gold-soft: #b8902a;
    --ink: #111111;
    --paper: #ffffff;
    --rule: #222222;
  }
  * { box-sizing: border-box; margin: 0; padding: 0; }
  html, body { width: 1200px; height: 1200px; overflow: hidden; background: var(--page); }
  .canvas { position: relative; width: 1200px; height: 1200px; }

  .label {
    position: absolute;
    background: var(--label-green);
    border-radius: 50% 50% 0 0 / 14% 14% 0 0;
    overflow: hidden;
    color: var(--gold);
    font-family: "Montserrat", sans-serif;
    text-align: center;
  }

  /* Front label */
  .label--front { left: 150px; top: 190px; width: 400px; height: 820px; }
  .key-pattern {
    position: absolute; inset: 0;
    background: linear-gradient(180deg, var(--key-green) 0%, var(--label-green) 50%, var(--key-green) 100%);
    opacity: .75;
  }
  .front-content { position: relative; padding-top: 78px; }
  .oil-type { font-weight: 800; letter-spacing: 1px; line-height: 1.15; }
  .oil-type--organic { font-size: 38px; }
  .oil-type--virgin { font-size: 36px; margin-top: 6px; }
  .product-name {
    font-family: "Playfair Display", serif;
    font-weight: 900; font-size: 80px; line-height: .95;
    margin-top: 14px; letter-spacing: 2px;
  }
  .olive-branch {
    width: 180px; height: 190px; margin: 34px auto 0;
    border-radius: 50%;
    background: radial-gradient(circle, rgba(214,169,46,.35) 0%, rgba(214,169,46,.08) 70%, transparent 100%);
  }
  .brand-name {
    font-weight: 800; font-size: 50px; line-height: 1.05;
    margin-top: 34px; color: var(--gold);
  }

  /* Back label */
  .label--back { left: 690px; top: 290px; width: 330px; height: 640px; background: var(--label-green-deep); }
  .back-content { position: relative; padding: 38px 22px 0; }
  .back-type { font-weight: 800; font-size: 19px; line-height: 1.2; letter-spacing: .5px; }
  .origin { font-family: "Montserrat", sans-serif; font-weight: 600; color: var(--paper); font-size: 21px; margin-top: 2px; }
  .back-info { display: flex; gap: 12px; margin-top: 8px; text-align: left; }
  .company-block { width: 108px; text-align: center; }
  .greek-flag { display: block; width: 54px; height: 36px; margin: 4px auto 12px; }
  .company-name { font-weight: 800; font-size: 20px; line-height: 1; color: var(--gold); }
  .company-suffix { font-weight: 800; font-size: 9px; letter-spacing: 2.5px; margin-top: 4px; color: var(--gold); }
  .company-address, .company-web {
    font-family: "Roboto Condensed", sans-serif; font-size: 9.5px; color: var(--gold); line-height: 1.45;
  }
  .company-address { margin-top: 6px; }
  .company-web { margin-top: 4px; font-size: 8.5px; word-break: break-all; }
  .product-story {
    flex: 1; font-family: "Roboto Condensed", sans-serif;
    font-size: 10.5px; line-height: 1.55; color: var(--paper);
  }

  .nutrition-facts {
    margin: 14px 8px 0; background: var(--paper); color: var(--ink);
    padding: 6px 7px 5px; text-align: left; font-family: "Archivo", sans-serif; font-size: 8px; line-height: 1.25;
  }
  .nf-title { font-weight: 900; font-size: 17px; line-height: 1; }
  .nf-rule-thick { border-top: 6px solid var(--rule); margin: 3px 0 2px; }
  .nf-rule { border-top: 1px solid var(--rule); }
  .nf-row { display: flex; justify-content: space-between; }
  .nf-row--indent { padding-left: 8px; }
  .nf-strong { font-weight: 800; }
  .nf-note { font-size: 6.5px; line-height: 1.25; margin-top: 3px; }

  .barcode-space {
    margin: 8px 8px 0; height: 78px; background: var(--paper); position: relative;
  }
  .best-by {
    position: absolute; left: 6px; bottom: 4px;
    font-family: "Roboto Condensed", sans-serif; font-size: 9px; color: var(--ink); text-align: left;
  }
</style>
</head>
<body>
<main class="canvas">

  <section class="label label--front" aria-label="Front label">
    <div class="key-pattern" role="img" aria-label="Greek key meander pattern in deep green"></div>
    <div class="front-content">
      <p class="oil-type oil-type--organic">ORGANIC</p>
      <p class="oil-type oil-type--virgin">EXTRA VIRGIN</p>
      <h1 class="product-name">OLIVE<br>OIL</h1>
      <div class="olive-branch" role="img" aria-label="Gold line illustration of an olive branch"></div>
      <p class="brand-name">Verdanto<br>Crest</p>
    </div>
  </section>

  <section class="label label--back" aria-label="Back label">
    <div class="back-content">
      <p class="back-type">ORGANIC<br>EXTRA VIRGIN</p>
      <p class="origin">Kalamata, Greece</p>

      <div class="back-info">
        <div class="company-block">
          <svg class="greek-flag" viewBox="0 0 27 18" aria-label="Flag of Greece" role="img">
            <rect width="27" height="18" fill="#0d5eaf"/>
            <g fill="#ffffff">
              <rect y="2" width="27" height="2"/>
              <rect y="6" width="27" height="2"/>
              <rect y="10" width="27" height="2"/>
              <rect y="14" width="27" height="2"/>
            </g>
            <rect width="10" height="10" fill="#0d5eaf"/>
            <rect x="4" width="2" height="10" fill="#ffffff"/>
            <rect y="4" width="10" height="2" fill="#ffffff"/>
          </svg>
          <p class="company-name">Verdanto Crest</p>
          <p class="company-suffix">IMPORTS LLC</p>
          <p class="company-address">Street Address line 1<br>City Address line 2</p>
          <p class="company-web">verdantocrestimports.example</p>
        </div>
        <p class="product-story">Lorem ipsum dolor sit amet, consectetuer adipiscing elit, sed diam nonummy nibh euismod. Lorem ipsum dolor sit amet, consectetuer adipiscing elit, sed diam nonummy nibh euismod. Lorem ipsum dolor sit amet, consectetuer adipiscing elit, sed diam euismod.</p>
      </div>

      <div class="nutrition-facts">
        <p class="nf-title">Nutrition Facts</p>
        <p>Serving Size 1 Tbsp (15 ml)</p>
        <p>Servings Per Container 200</p>
        <div class="nf-rule-thick"></div>
        <p class="nf-strong" style="font-size:6.5px">Amount Per Serving</p>
        <div class="nf-row"><span><b>Calories</b> 120</span><span>Fat Cal 120</span></div>
        <div class="nf-rule-thick" style="border-top-width:3px"></div>
        <div class="nf-row" style="justify-content:flex-end;font-size:6.5px"><span>% Daily Value*</span></div>
        <div class="nf-row"><span><b>Total Fat</b> 14g</span><span>22%</span></div>
        <div class="nf-row nf-row--indent"><span>Saturated Fat 2g</span><span>10%</span></div>
        <div class="nf-row nf-row--indent"><span>Trans Fat 0g</span><span>0%</span></div>
        <div class="nf-row nf-row--indent"><span>Polyunsaturated Fat 1.6g</span><span>0%</span></div>
        <div class="nf-row nf-row--indent"><span>Monounsaturated Fat 10.4g</span><span>0%</span></div>
        <div class="nf-row"><span><b>Cholesterol</b> 0mg</span><span>0%</span></div>
        <div class="nf-row"><span><b>Sodium</b> 0mg</span><span>0%</span></div>
        <div class="nf-row"><span><b>Total Carbohydrate</b> 0g</span><span>0%</span></div>
        <div class="nf-row"><span><b>Protein</b> 0g</span><span>0%</span></div>
        <div class="nf-rule-thick" style="border-top-width:3px"></div>
        <p class="nf-note">Not a significant source of dietary fiber, sugars, vitamin A, vitamin C, calcium and iron.</p>
        <p class="nf-note">*Percent Daily Values are based on a 2,000 calorie diet.</p>
      </div>

      <div class="barcode-space" aria-label="Space reserved for barcode">
        <p class="best-by">BEST BY DATE:</p>
      </div>
    </div>
  </section>

</main>
</body>
</html>
```